Professional business cards for real estate development company

I need business cards for my new real estate development company. The company, "KORVA" is a real estate development, investment, and advisory firm with a focus on multifamily, office, and mixed-use projects across primary and secondary markets in the Southeast United States.

Style preference is modern

Industry/Entity Type

Real Estate Development

Contact Information for Business Card

The business cards need to include:
Name
Title
Mailing Address
Phone Number
Web Address

Logo is attached. I would like white to be the primary color with incorporation of the company colors: #232D3A and #B5A451

Font styles to use
Other font styles liked:
• Montserrat, Avenir

Requirements
Must have
• Company Logo. No need to include the company name since the name is in the logo.
Should not have
• No line type designs

```html
<!DOCTYPE html>
<html lang="en">
<head>
<meta charset="utf-8">
<title>KORVA Business Cards</title>
<link rel="stylesheet" href="https://fonts.googleapis.com/css2?family=Montserrat:wght@400;500;600;700&display=swap">
<style>
  :root {
    --navy: #232D3A;
    --navy-deep: #1E2938;
    --gold: #B5A451;
    --white: #FFFFFF;
    --backdrop: #2A2A2C;
  }
  * { box-sizing: border-box; margin: 0; padding: 0; }
  html, body {
    width: 1200px; height: 800px; overflow: hidden;
    background: var(--backdrop);
    font-family: "Montserrat", sans-serif;
  }
  .stage {
    position: relative; width: 1200px; height: 800px;
    display: flex; align-items: center; justify-content: center; gap: 40px;
  }
  .card {
    position: relative; width: 540px; height: 309px;
    border-radius: 16px; overflow: hidden;
  }

  /* Front */
  .card-front { background: var(--white); }
  .front-logo {
    position: absolute; left: 200px; top: 52px;
    display: flex; align-items: center; gap: 12px;
    color: var(--navy); font-weight: 700; font-size: 48px; letter-spacing: 4px;
  }
  .front-logo .mark { width: 22px; height: 22px; background: var(--navy); }
  .name-rule {
    position: absolute; top: 140px; left: 0; right: 0; height: 2px;
  }
  .name-rule .seg { position: absolute; top: 0; height: 2px; background: var(--navy); }
  .name-rule .seg-left { left: 0; width: 22px; }
  .name-rule .seg-right { left: 250px; right: 0; }
  .holder {
    position: absolute; left: 34px; top: 129px;
    font-size: 14px; font-weight: 700; color: var(--navy); letter-spacing: 0.5px;
    white-space: nowrap;
  }
  .holder .role { color: var(--gold); font-size: 11px; margin-left: 4px; }
  .contact-band {
    position: absolute; left: 0; right: 0; top: 152px; height: 104px;
    background: var(--navy-deep);
  }
  .contact-list { position: absolute; left: 28px; top: 16px; list-style: none; }
  .contact-list li {
    display: flex; align-items: center; gap: 10px;
    color: var(--white); font-size: 12.5px; line-height: 23px;
  }
  .contact-list svg, .address svg { flex: none; }
  .address {
    position: absolute; left: 316px; top: 18px;
    display: flex; gap: 8px; color: var(--white); font-size: 12.5px; line-height: 19px;
  }
  .white-gap { position: absolute; left: 0; right: 0; top: 256px; height: 4px; background: var(--white); }
  .gold-band {
    position: absolute; left: 0; right: 0; bottom: 0; height: 49px;
    background: var(--gold);
    display: flex; align-items: center; justify-content: center;
  }
  .services {
    color: var(--white); font-size: 11.5px; font-weight: 500; letter-spacing: 0.6px;
  }

  /* Back */
  .card-back { background: var(--navy-deep); }
  .back-logo {
    position: absolute; left: 0; right: 0; top: 100px;
    display: flex; align-items: center; justify-content: center; gap: 14px;
    color: var(--white); font-weight: 700; font-size: 54px; letter-spacing: 5px;
  }
  .back-logo .mark { width: 24px; height: 24px; background: var(--white); }
  .back-gap { position: absolute; left: 0; right: 0; bottom: 49px; height: 4px; background: var(--white); }
  .back-band {
    position: absolute; left: 0; right: 0; bottom: 0; height: 49px;
    background: var(--gold);
    display: flex; align-items: center; justify-content: center;
  }
  .back-web { color: var(--navy); font-size: 13px; font-weight: 600; letter-spacing: 1.5px; }
</style>
</head>
<body>
<main class="stage">

  <section class="card card-front" aria-label="Business card front">
    <div class="front-logo"><span class="mark"></span><span class="brand">KORVA</span></div>

    <div class="name-rule"><span class="seg seg-left"></span><span class="seg seg-right"></span></div>
    <p class="holder">ELLIS MARDEN <span class="role">DIRECTOR</span></p>

    <div class="contact-band">
      <ul class="contact-list">
        <li>
          <svg width="13" height="13" viewBox="0 0 24 24" aria-hidden="true"><path fill="#B5A451" d="M6.6 10.8a15.1 15.1 0 0 0 6.6 6.6l2.2-2.2c.3-.3.7-.4 1-.2 1.1.4 2.3.6 3.6.6.6 0 1 .4 1 1V20c0 .6-.4 1-1 1A17 17 0 0 1 3 4c0-.6.4-1 1-1h3.5c.6 0 1 .4 1 1 0 1.3.2 2.5.6 3.6.1.3 0 .7-.2 1z"/></svg>
          <span>555-210-4873</span>
        </li>
        <li>
          <svg width="13" height="13" viewBox="0 0 24 24" aria-hidden="true"><path fill="#B5A451" d="M2 5h20v14H2z"/><path fill="none" stroke="#1E2938" stroke-width="1.8" d="M2 5l10 8 10-8"/></svg>
          <span>info@korvadevelopment.com</span>
        </li>
        <li>
          <svg width="13" height="13" viewBox="0 0 24 24" aria-hidden="true"><g fill="none" stroke="#B5A451" stroke-width="1.8"><circle cx="12" cy="12" r="10"/><ellipse cx="12" cy="12" rx="4.5" ry="10"/><path d="M2 12h20M4 7h16M4 17h16"/></g></svg>
          <span>www.korvadevelopment.com</span>
        </li>
      </ul>
      <div class="address">
        <svg width="12" height="16" viewBox="0 0 24 32" aria-hidden="true"><path fill="#B5A451" d="M12 0C5.4 0 0 5.4 0 12c0 9 12 20 12 20s12-11 12-20C24 5.4 18.6 0 12 0zm0 17a5 5 0 1 1 0-10 5 5 0 0 1 0 10z"/></svg>
        <p>118 Harlow Street<br>Suite 300, Ashford<br>GA 30512</p>
      </div>
    </div>
    <div class="white-gap"></div>
    <div class="gold-band"><p class="services">REAL ESTATE DEVELOPMENT • INVESTMENT • ADVISORY</p></div>
  </section>

  <section class="card card-back" aria-label="Business card back">
    <div class="back-logo"><span class="mark"></span><span class="brand">KORVA</span></div>
    <div class="back-gap"></div>
    <div class="back-band"><p class="back-web">WWW.KORVADEVELOPMENT.COM</p></div>
  </section>

</main>
</body>
</html>
```